Aldercrest Chiropractic Rehabilitation and Wellness
Business Card, Portfolio Folder, Stationary, Postcard
Simple
Marlow Tenney
Doctor of Chiropractic
518 Verbena Ridge Avenue
Chico, CA 95926
marlow@alderbrook.com
www.alderbrook.com
Fonts are TrajanPro and Corbel
Logo and URL or just logo
Logo
jpg Logo

```html
<!DOCTYPE html>
<html lang="en">
<head>
<meta charset="utf-8">
<title>Aldercrest Chiropractic – Stationery Set</title>
<link href="https://fonts.googleapis.com/css2?family=Source+Sans+3:wght@400;600&display=swap" rel="stylesheet">
<style>
  :root{
    --bg:#eceae6;
    --paper:#ffffff;
    --edge:#d9d9d9;
    --blue:#1f63a6;
    --green:#8cc63f;
    --ink:#5a5a5a;
  }
  *{box-sizing:border-box;margin:0;padding:0}
  html,body{width:1200px;height:526px;overflow:hidden;background:var(--bg)}
  body{position:relative;font-family:"Source Sans 3",sans-serif;color:var(--ink)}
  .sheet{position:absolute;background:var(--paper);border:1px solid var(--edge);box-shadow:0 2px 6px rgba(0,0,0,.12);overflow:hidden}

  .brand{display:flex;align-items:center;gap:8px}
  .brand-square{flex:none;background:var(--green)}
  .brand-name{font-family:"Source Sans 3",sans-serif;font-weight:600;color:var(--blue);line-height:1.15}
  .micro{font-size:6px;color:var(--ink);white-space:nowrap}

  /* Folder */
  .folder{left:40px;top:40px;width:540px;height:420px;border:none;box-shadow:none;background:none;overflow:visible}
  .folder-panel{position:absolute;top:0;width:270px;height:420px;background:var(--paper);border:1px solid var(--edge);box-shadow:0 2px 6px rgba(0,0,0,.12)}
  .folder-panel.left{left:0}
  .folder-panel.right{left:270px;border-left:1px dashed #e3e3e3}
  .folder-panel .contact{position:absolute;top:14px;left:40px}
  .folder-panel .brand{position:absolute;left:36px;top:160px}
  .folder-panel .brand-name{font-size:15px;width:180px}
  .folder-pocket{position:absolute;left:0;bottom:0;width:540px;height:120px}
  .pocket-brand{position:absolute;left:30px;bottom:26px;transform:rotate(180deg)}
  .pocket-brand .brand-name{font-size:11px;width:150px}

  /* Letterhead */
  .letterhead{left:606px;top:120px;width:206px;height:286px}
  .letterhead .brand{position:absolute;left:18px;top:18px}
  .letterhead .brand-name{font-size:8px;width:130px}
  .letterhead .contact{position:absolute;top:50px;left:18px}
  .letterhead .footer{position:absolute;bottom:10px;left:18px}

  /* Fax sheet */
  .fax{left:828px;top:28px;width:206px;height:270px}
  .fax .brand{position:absolute;left:16px;top:14px}
  .fax .brand-name{font-size:8px;width:120px}
  .fax .contact{position:absolute;top:46px;left:16px}
  .fax-title{position:absolute;right:16px;top:18px;font-weight:600;font-size:11px;color:var(--blue)}
  .fax-table{position:absolute;left:16px;top:64px;width:120px;border-collapse:collapse}
  .fax-table td{border:1px solid #cfcfcf;font-size:6px;height:11px;padding:0 3px}
  .fax-table td:first-child{width:34px;background:#f3f3f3}
  .fax-checks{position:absolute;left:16px;top:134px;display:flex;gap:10px}
  .fax-checks span{font-size:6px;display:flex;align-items:center;gap:3px}
  .fax-checks i{width:6px;height:6px;border:1px solid #aaa;display:inline-block}

  /* Business cards */
  .card{width:128px;height:74px}
  .card-front{left:1050px;top:150px}
  .card-front .brand{position:absolute;left:12px;top:24px}
  .card-front .brand-name{font-size:7px;width:90px}
  .card-back{left:1050px;top:236px}
  .card-back .person{position:absolute;left:12px;top:12px}
  .card-back .person strong{display:block;font-size:8px;color:var(--blue);font-weight:600}
  .card-back .person span{display:block;font-size:6px}
  .card-back .details{position:absolute;left:12px;bottom:8px;line-height:1.3}

  /* Envelope */
  .envelope{left:828px;top:326px;width:350px;height:140px}
  .envelope .brand{position:absolute;left:16px;top:14px}
  .envelope .brand-name{font-size:8px;width:130px}
  .envelope .contact{position:absolute;left:16px;top:46px}
  .envelope .stripe{position:absolute;left:0;bottom:0;width:100%;height:4px;background:var(--green)}
</style>
</head>
<body>

<section class="sheet folder" aria-label="Presentation folder">
  <div class="folder-panel left"></div>
  <div class="folder-panel right">
    <p class="contact micro">518 Verbena Ridge Avenue, Chico, CA 95926 · (530) 555-0148 · www.alderbrook.com</p>
    <div class="brand">
      <span class="brand-square" style="width:22px;height:22px"></span>
      <span class="brand-name">Aldercrest Chiropractic Rehabilitation and Wellness</span>
    </div>
  </div>
  <svg class="folder-pocket" viewBox="0 0 540 120" aria-hidden="true">
    <path d="M0 8 H250 L270 40 L290 8 H540 V120 H0 Z" fill="#ffffff" stroke="#d4d4d4"/>
  </svg>
  <div class="brand pocket-brand">
    <span class="brand-square" style="width:16px;height:16px"></span>
    <span class="brand-name">Aldercrest Chiropractic Rehabilitation and Wellness</span>
  </div>
</section>

<section class="sheet letterhead" aria-label="Letterhead">
  <div class="brand">
    <span class="brand-square" style="width:10px;height:10px"></span>
    <span class="brand-name">Aldercrest Chiropractic Rehabilitation and Wellness</span>
  </div>
  <p class="contact micro">518 Verbena Ridge Avenue · Chico, CA 95926</p>
  <p class="footer micro">www.alderbrook.com</p>
</section>

<section class="sheet fax" aria-label="Fax cover sheet">
  <div class="brand">
    <span class="brand-square" style="width:10px;height:10px"></span>
    <span class="brand-name">Aldercrest Chiropractic Rehabilitation and Wellness</span>
  </div>
  <p class="contact micro">518 Verbena Ridge Avenue · marlow@alderbrook.com</p>
  <span class="fax-title">FAX</span>
  <table class="fax-table">
    <tr><td>To</td><td></td></tr>
    <tr><td>From</td><td></td></tr>
    <tr><td>Fax</td><td></td></tr>
    <tr><td>Date</td><td></td></tr>
    <tr><td>Re</td><td></td></tr>
  </table>
  <div class="fax-checks">
    <span><i></i>Urgent</span>
    <span><i></i>Review</span>
    <span><i></i>Reply</span>
  </div>
</section>

<section class="sheet card card-front" aria-label="Business card front">
  <div class="brand">
    <span class="brand-square" style="width:9px;height:9px"></span>
    <span class="brand-name">Aldercrest Chiropractic Rehabilitation and Wellness</span>
  </div>
</section>

<section class="sheet card card-back" aria-label="Business card back">
  <div class="person">
    <strong>Marlow Tenney</strong>
    <span>Doctor of Chiropractic</span>
  </div>
  <div class="details micro">
    518 Verbena Ridge Avenue<br>Chico, CA 95926<br>marlow@alderbrook.com
  </div>
</section>

<section class="sheet envelope" aria-label="Envelope">
  <div class="brand">
    <span class="brand-square" style="width:10px;height:10px"></span>
    <span class="brand-name">Aldercrest Chiropractic Rehabilitation and Wellness</span>
  </div>
  <p class="contact micro">518 Verbena Ridge Avenue · Chico, CA 95926</p>
  <div class="stripe"></div>
</section>

</body>
</html>
```